Business Image

I have recently had a new company logo made up and require some new business cards to go with it.

Target Market(s)

Developers & high worth clients.

Industry/Entity Type

Business

Contact Information for Business Card

The business is in the construction/management industry. It needs to be classy but have a industrial feel. I would like the business card to be a elegant presentation in itself.

Requirements
Must have
• Current logo & company name. Colouring needs to be the same as the current design also.
Nice to have
• A few different designs & presentations of single and double sided business cards.

```html
<!DOCTYPE html>
<html lang="en">
<head>
<meta charset="utf-8">
<title>Halvermark – Business Card</title>
<link href="https://fonts.googleapis.com/css2?family=Roboto:wght@400;500;700&display=swap" rel="stylesheet">
<style>
  :root {
    --steel-blue: #4677a0;
    --charcoal: #505052;
    --ink: #2f2f31;
    --card: #ffffff;
    --backdrop: #e8e5e0;
    --ghost: #e6e9ef;
  }
  * { margin: 0; padding: 0; box-sizing: border-box; }
  html, body { width: 900px; height: 1200px; overflow: hidden; }
  body {
    background: var(--backdrop);
    font-family: "Roboto", Arial, sans-serif;
    position: relative;
  }
  .card {
    position: absolute;
    left: 133px;
    width: 642px;
    height: 376px;
    background: var(--card);
    overflow: hidden;
    box-shadow: 0 2px 10px rgba(0,0,0,0.12);
  }
  .card--front { top: 192px; }
  .card--back { top: 634px; }

  .wordmark {
    font-family: "Roboto", Arial, sans-serif;
    font-weight: 700;
    color: var(--steel-blue);
    letter-spacing: 1px;
    line-height: 1;
    white-space: nowrap;
  }
  .card--front .wordmark {
    position: absolute;
    left: 52px;
    top: 58px;
    font-size: 36px;
  }
  .brand-block {
    position: absolute;
    left: 360px;
    top: 52px;
    width: 250px;
    height: 250px;
    background: var(--steel-blue);
  }

  .holder {
    position: absolute;
    left: 52px;
    top: 140px;
  }
  .holder-name { font-size: 21px; font-weight: 500; color: var(--ink); }
  .holder-title { font-size: 14px; color: var(--steel-blue); margin-top: 4px; }

  .contact-list {
    position: absolute;
    left: 52px;
    top: 200px;
    list-style: none;
  }
  .contact-list li {
    display: flex;
    align-items: center;
    font-size: 14px;
    color: var(--ink);
    height: 22px;
  }
  .contact-list svg { width: 16px; height: 14px; margin-right: 10px; fill: var(--steel-blue); }

  .address {
    position: absolute;
    left: 52px;
    top: 297px;
    font-size: 14px;
    line-height: 22px;
    color: var(--ink);
    font-style: normal;
  }

  .ghost-block {
    position: absolute;
    left: -30px;
    top: 20px;
    width: 270px;
    height: 340px;
    background: var(--ghost);
  }
  .back-lockup {
    position: absolute;
    left: 182px;
    top: 82px;
    display: flex;
    flex-direction: column;
    align-items: flex-start;
  }
  .back-lockup .mark-square {
    width: 100px;
    height: 100px;
    background: var(--steel-blue);
    margin-left: 87px;
    margin-bottom: 36px;
  }
  .back-lockup .wordmark { font-size: 40px; }
</style>
</head>
<body>

  <section class="card card--front">
    <div class="wordmark">HALVERMARK</div>

    <div class="holder">
      <div class="holder-name">Daniel Whitford</div>
      <div class="holder-title">Managing Director</div>
    </div>

    <ul class="contact-list">
      <li>
        <svg viewBox="0 0 16 14" aria-hidden="true"><path d="M1 4c0-2 3-3 7-3s7 1 7 3v1h-3V4H4v1H1z"/><path d="M3 7l2-2h6l2 2v6H3z"/></svg>
        555.010.4821
      </li>
      <li>
        <svg viewBox="0 0 16 14" aria-hidden="true"><rect x="4" y="0" width="8" height="4"/><rect x="0" y="5" width="16" height="6" rx="1"/><rect x="4" y="9" width="8" height="5"/></svg>
        555.010.7390
      </li>
      <li>
        <svg viewBox="0 0 16 14" aria-hidden="true"><path d="M0 2h16v10H0z"/><path d="M1 3l7 5 7-5" fill="none" stroke="#fff" stroke-width="1.3"/></svg>
        info@halvermark.com
      </li>
      <li>
        <svg viewBox="0 0 16 14" aria-hidden="true"><circle cx="8" cy="7" r="7"/><path d="M1 7h14M8 0v14M3 3h10M3 11h10" stroke="#fff" stroke-width="0.9" fill="none"/></svg>
        www.halvermark.com
      </li>
    </ul>

    <address class="address">480 Granite Way<br>Millbrook City 84120</address>

    <div class="brand-block" aria-hidden="true"></div>
  </section>

  <section class="card card--back">
    <div class="ghost-block" aria-hidden="true"></div>
    <div class="back-lockup">
      <div class="mark-square" aria-hidden="true"></div>
      <div class="wordmark">HALVERMARK</div>
    </div>
  </section>

</body>
</html>
```